Wordpress Corporate Website for New Business

We need a corporate website created which will act as a professional shop window for our new business. We do not need special features like merchant facilities or chatbots. The attachment shows suggested key sections as well as some possible wording. Various versions of the company logo have been attached as well to give different options to play with. We are looking for an option which is easy for us to take over and manage moving forward should we need to make minor updates.

Target Market(s)

Corporate entities

Industry/Entity Type

Private share auctions

Coding

Coded - Design and coding required

```html
<!DOCTYPE html>
<html lang="en">
<head>
<meta charset="utf-8">
<title>TenderWave – Private Share Auctions</title>
<link rel="stylesheet" href="https://fonts.googleapis.com/css2?family=Montserrat:wght@500;600;700;800&family=Lato:wght@400;700&display=swap">
<style>
:root{
  --purple:#8c0088;
  --navy:#0c0a93;
  --navy-card:#2723a6;
  --ink:#141342;
  --footer:#0a0a3c;
  --text:#2a2a3a;
  --white:#ffffff;
}
*{box-sizing:border-box;margin:0;padding:0}
html,body{width:1200px;height:4112px;overflow:hidden;background:var(--white)}
body{font-family:'Lato',sans-serif;color:var(--text)}
.page{position:relative;width:1200px;height:4112px;overflow:hidden}
.abs{position:absolute}
.heading{font-family:'Montserrat',sans-serif;font-weight:700;color:var(--ink)}
.accent{color:var(--purple)}
.navy{color:var(--navy)}

/* header */
.site-header{position:absolute;left:0;top:0;width:1200px;height:67px;background:var(--white);z-index:3}
.brand{position:absolute;left:142px;top:16px;display:flex;align-items:center;gap:8px;font-family:'Montserrat',sans-serif;font-weight:700;font-size:30px;color:var(--purple)}
.brand-dot{width:30px;height:30px;border-radius:50%;background:var(--navy);flex:none}
.main-nav{position:absolute;right:142px;top:24px;display:flex;gap:30px;font-size:12px;color:var(--ink)}
.main-nav .active{color:var(--purple);font-weight:700}

/* hero */
.hero-photo{position:absolute;left:0;top:67px;width:1200px;height:520px;background:linear-gradient(180deg,#2c3550 0%,#4a5877 40%,#1d2238 100%)}
.hero-title{position:absolute;top:450px;width:1200px;text-align:center;font-family:'Montserrat',sans-serif;font-weight:800;font-size:38px;color:var(--white);letter-spacing:.5px}
.btn-pill{position:absolute;display:flex;align-items:center;height:34px;padding:0 18px 0 6px;border-radius:17px;background:var(--white);font-size:12px;color:var(--ink);gap:12px}
.btn-pill .dot{width:28px;height:28px;border-radius:50%;background:var(--navy)}

/* about */
.about-mark{position:absolute;left:140px;top:700px;width:315px;height:315px;border-radius:50%;background:radial-gradient(circle at 55% 50%,#2c32c8 0%,#4a1fa8 45%,#9a1db0 100%)}
.about-title{position:absolute;left:564px;top:772px;font-size:38px}
.about-text{position:absolute;left:564px;top:830px;width:500px;font-size:12px;line-height:28px;color:#333}

/* team */
.team-title{position:absolute;top:1205px;width:1200px;text-align:center;font-size:38px;color:var(--white)}
.member{position:absolute;top:1290px;width:210px;text-align:center;color:var(--white)}
.member-photo{width:176px;height:176px;border-radius:50%;margin:0 auto;background:linear-gradient(160deg,#c9b7ae,#6d5a58);border:3px solid var(--white)}
.member-ring{position:absolute;left:8px;top:-8px;width:194px;height:194px;border-radius:50%;border:4px solid transparent;border-top-color:var(--navy);border-right-color:var(--navy);transform:rotate(10deg)}
.member-ring.left{border-top-color:transparent;border-right-color:transparent;border-bottom-color:var(--navy);border-left-color:var(--navy)}
.member-name{margin-top:24px;font-family:'Montserrat',sans-serif;font-weight:700;font-size:14px}
.member-role{font-size:10px;margin-top:2px}
.member-bio{font-size:11.5px;line-height:20px;margin:8px auto 0;width:185px}
.socials{display:flex;justify-content:center;gap:8px;margin-top:12px}
.socials span{width:27px;height:27px;border-radius:50%;border:1.5px solid var(--white)}
.pager{position:absolute;top:1673px;left:562px;display:flex;gap:9px;align-items:center}
.pager span{width:12px;height:12px;border-radius:50%;background:#d5a6d4}
.pager .on{width:16px;height:16px;background:#d13ad0;border:2px solid #f0c5f0}

/* key features */
.feature{position:absolute;left:142px;width:520px}
.feature svg{position:absolute;left:0;top:0}
.feature h3{margin-left:75px;font-family:'Montserrat',sans-serif;font-weight:600;font-size:22px;color:var(--ink)}
.feature p{margin-left:75px;margin-top:14px;width:430px;font-size:12px;line-height:21px;color:#333}
.kf-title{position:absolute;left:755px;top:1920px;font-size:38px;line-height:44px}
.kf-text{position:absolute;left:755px;top:2032px;width:305px;font-size:14.5px;line-height:23px;color:#333}

/* why choose */
.why-title{position:absolute;top:2350px;width:1200px;text-align:center;font-size:38px;color:var(--white)}
.card{position:absolute;width:211px;height:316px;background:var(--navy-card);border-radius:6px;text-align:center;color:var(--white);padding:38px 12px 0}
.card svg{display:block;margin:0 auto}
.card h4{margin-top:26px;font-family:'Montserrat',sans-serif;font-weight:600;font-size:14px;white-space:nowrap}
.card p{margin-top:12px;font-size:11px;line-height:19px;color:#dcdcf5;padding:0 4px}

/* faq */
.faq-title{position:absolute;top:3360px;width:1200px;text-align:center;font-size:38px}
.faq-spine{position:absolute;left:285px;top:3470px;width:2px;height:290px;background:#cfcfe0}
.faq-item{position:absolute;left:265px;width:661px;height:36px}
.faq-num{position:absolute;left:0;top:-2px;width:40px;height:40px;border-radius:50%;background:#eceaf2;border:3px solid var(--white);box-shadow:0 0 0 1px #d3d1de;display:flex;align-items:center;justify-content:center;font-family:'Montserrat',sans-serif;font-weight:700;font-size:13px;color:var(--ink)}
.faq-q{position:absolute;left:38px;top:0;right:0;height:36px;border:1px solid #d8d6e4;border-left:none;background:var(--white);display:flex;align-items:center;padding:0 16px 0 20px;font-size:11.5px;color:var(--ink)}
.faq-q b{margin-left:auto;font-size:18px;color:var(--purple);font-weight:700}
.faq-item.open .faq-num{background:var(--purple);color:var(--white)}
.faq-item.open .faq-q{background:var(--purple);color:var(--white);border-color:var(--purple)}
.faq-item.open .faq-q b{color:var(--white)}
.faq-answer{position:absolute;left:323px;top:3612px;width:600px;font-size:11.5px;line-height:19px;color:#333}

/* footer */
.footer-band{position:absolute;left:0;top:3905px;width:1200px;height:150px;background:var(--footer)}
.footer-row{position:absolute;left:0;top:3962px;width:1200px;display:flex;justify-content:center;align-items:center;gap:44px;color:var(--white)}
.contact{display:flex;align-items:center;gap:10px}
.contact small{display:block;font-size:11px}
.contact strong{font-size:14px;font-weight:700}
.footer-brand{display:flex;align-items:center;gap:10px;font-family:'Montserrat',sans-serif;font-weight:700;font-size:36px;color:var(--white)}
.footer-brand .brand-dot{width:40px;height:40px;background:var(--white)}
.copyright-bar{position:absolute;left:0;top:4054px;width:1200px;height:58px;background:var(--purple);color:var(--white);font-size:11.5px}
.copyright-bar p{position:absolute;left:142px;top:21px}
.copyright-bar span{position:absolute;left:1023px;top:12px;width:34px;height:34px;border-radius:50%;background:var(--white)}
</style>
</head>
<body>
<div class="page">

  <header class="site-header">
    <div class="brand"><span class="brand-dot"></span>TenderWave</div>
    <nav class="main-nav">
      <span class="active">Home</span><span>About Us</span><span>Team</span><span>Key Features</span><span>Why Choose Us</span><span>Contact Us</span>
    </nav>
  </header>

  <div class="hero-photo" role="img" aria-label="Businessman in a dark suit touching a glowing digital auction-gavel interface"></div>
  <svg class="abs" style="left:0;top:470px" width="1200" height="140" viewBox="0 0 1200 140">
    <path d="M0 60 Q600 170 1200 60 L1200 140 L0 140Z" fill="#fff"/>
    <path d="M142 92 Q600 122 1058 92" stroke="#0c0a93" stroke-width="6" fill="none"/>
  </svg>
  <h1 class="hero-title">RETAIN CONTROL, UNLOCK LIQUIDITY</h1>
  <div class="btn-pill" style="left:514px;top:517px"><span class="dot"></span>Contact Us Today</div>

  <div class="about-mark" role="img" aria-label="Large brand mark with private equity imagery"></div>
  <h2 class="heading about-title">About <span class="accent">Tender</span><span class="navy">Wave</span></h2>
  <p class="about-text">At TenderWave, we empower private companies to take control of their share transactions without the hassle of third-party involvement. Our innovative share exchange platform is designed to connect pre-approved buyers and sellers directly, fostering a secure and efficient environment for trading ownership in private enterprises.</p>

  <svg class="abs" style="left:0;top:1125px" width="1200" height="670" viewBox="0 0 1200 670">
    <path d="M142 30 Q600 0 1058 30" stroke="#0c0a93" stroke-width="6" fill="none"/>
    <path d="M0 70 Q600 -20 1200 70 L1200 590 Q600 680 0 590Z" fill="#8c0088"/>
    <path d="M142 625 Q600 665 1058 625" stroke="#0c0a93" stroke-width="6" fill="none"/>
  </svg>
  <h2 class="heading team-title">Meet Our Team</h2>

  <div class="member" style="left:142px">
    <div class="member-ring left"></div>
    <div class="member-photo" role="img" aria-label="Portrait photo of team member"></div>
    <div class="member-name">Maren Holt</div><div class="member-role">Duis Autem</div>
    <p class="member-bio">Lorem ipsum dolor sit amet, consectetuer adipiscing elit, sed diam nonummy nibh euismod.</p>
    <div class="socials"><span></span><span></span><span></span></div>
  </div>
  <div class="member" style="left:379px">
    <div class="member-ring left"></div>
    <div class="member-photo" role="img" aria-label="Portrait photo of team member"></div>
    <div class="member-name">Tobias Reyes</div><div class="member-role">Duis Autem</div>
    <p class="member-bio">Lorem ipsum dolor sit amet, consectetuer adipiscing elit, sed diam nonummy nibh euismod.</p>
    <div class="socials"><span></span><span></span><span></span></div>
  </div>
  <div class="member" style="left:616px">
    <div class="member-ring"></div>
    <div class="member-photo" role="img" aria-label="Portrait photo of team member"></div>
    <div class="member-name">Ilse Park</div><div class="member-role">Duis Autem</div>
    <p class="member-bio">Lorem ipsum dolor sit amet, consectetuer adipiscing elit, sed diam nonummy nibh euismod.</p>
    <div class="socials"><span></span><span></span><span></span></div>
  </div>
  <div class="member" style="left:854px">
    <div class="member-ring"></div>
    <div class="member-photo" role="img" aria-label="Portrait photo of team member"></div>
    <div class="member-name">Dorian Lee</div><div class="member-role">Duis Autem</div>
    <p class="member-bio">Lorem ipsum dolor sit amet, consectetuer adipiscing elit, sed diam nonummy nibh euismod.</p>
    <div class="socials"><span></span><span></span><span></span></div>
  </div>
  <div class="pager"><span></span><span class="on"></span><span></span><span></span></div>

  <div class="feature" style="top:1900px">
    <svg width="48" height="48" viewBox="0 0 48 48" fill="none" stroke="#8c0088" stroke-width="2"><rect x="8" y="6" width="18" height="36"/><rect x="26" y="18" width="14" height="24"/><path d="M4 42h40M12 12h4M18 12h4M12 20h4M18 20h4M12 28h4M18 28h4M30 24h6M30 32h6"/></svg>
    <h3>Company</h3>
    <p>This might explain what we do to help the company roll this out and the process, including engagement with shareholders for setting up the user access, technical support provided and the information provided at the close of the auction</p>
  </div>
  <div class="feature" style="top:2050px">
    <svg width="48" height="48" viewBox="0 0 48 48" fill="none" stroke="#8c0088" stroke-width="2"><circle cx="24" cy="10" r="6"/><circle cx="10" cy="32" r="5"/><circle cx="24" cy="32" r="5"/><circle cx="38" cy="32" r="5"/><path d="M24 16v10M10 26l14-8 14 8M3 46q7-8 14 0M17 46q7-8 14 0M31 46q7-8 14 0"/></svg>
    <h3>Shareholder</h3>
    <p>Example of the login process, what features the platform has and what happens post a transaction.</p>
  </div>
  <h2 class="heading kf-title">Our<br><span class="accent">Key</span> Features</h2>
  <p class="kf-text">Looking at having options to click on two different prominent buttons which then take you directly to separate spaces:</p>

  <svg class="abs" style="left:0;top:2240px" width="1200" height="1010" viewBox="0 0 1200 1010">
    <path d="M142 50 Q600 10 1058 50" stroke="#8c0088" stroke-width="6" fill="none"/>
    <path d="M0 92 Q600 -5 1200 92 L1200 945 Q600 1040 0 945Z" fill="#0c0a93"/>
    <path d="M142 985 Q600 1025 1058 985" stroke="#8c0088" stroke-width="6" fill="none"/>
  </svg>
  <h2 class="heading why-title">Why Choose TenderWave</h2>

  <div class="card" style="left:142px;top:2434px">
    <svg width="48" height="48" viewBox="0 0 48 48" fill="none" stroke="#fff" stroke-width="1.8"><rect x="10" y="4" width="24" height="20"/><rect x="4" y="24" width="30" height="18"/><circle cx="36" cy="36" r="7"/><path d="M10 32h14M10 37h10"/></svg>
    <h4>Retain Control</h4>
    <p>Companies can maintain control over who participates in their auctions. This control is essential for preserving the company's culture, protecting sensitive information, and ensuring that only pre-approved parties are involved.</p>
  </div>
  <div class="card" style="left:377px;top:2434px">
    <svg width="48" height="48" viewBox="0 0 48 48" fill="none" stroke="#fff" stroke-width="1.8"><circle cx="24" cy="30" r="10"/><path d="M24 4v12M8 10l8 8M40 10l-8 8M4 26h8M36 26h8M21 27q3-3 6 0q0 4-6 5q0 4 6 3"/></svg>
    <h4>Unlock Liquidity</h4>
    <p>TenderWave provides a structured marketplace which facilitates efficient and easy share transactions, creating a level of liquidity not previously experienced by private company investors.</p>
  </div>
  <div class="card" style="left:612px;top:2434px">
    <svg width="48" height="48" viewBox="0 0 48 48" fill="none" stroke="#fff" stroke-width="1.8"><circle cx="14" cy="14" r="9"/><circle cx="34" cy="34" r="9"/><path d="M26 8h14v10M22 40H8V30M36 14l4 4 4-4M4 34l4-4 4 4"/></svg>
    <h4>Direct Transactions</h4>
    <p>Say goodbye to intermediaries. Our platform enables shareholders in private companies to trade shares directly, ensuring transparency and efficiency in every transaction.</p>
  </div>
  <div class="card" style="left:846px;top:2434px">
    <svg width="48" height="48" viewBox="0 0 48 48" fill="none" stroke="#fff" stroke-width="1.8"><rect x="10" y="3" width="28" height="42"/><path d="M15 10h18M15 15h18M15 20h12"/><rect x="18" y="30" width="12" height="10"/><path d="M20 30v-3a4 4 0 0 1 8 0v3"/></svg>
    <h4>Secure and Confidential</h4>
    <p>We understand the importance of privacy. Our security measures safeguard your sensitive information, providing a secure space for seamless share trading.</p>
  </div>
  <div class="card" style="left:260px;top:2772px">
    <svg width="48" height="48" viewBox="0 0 48 48" fill="none" stroke="#fff" stroke-width="1.8"><circle cx="24" cy="24" r="8"/><circle cx="24" cy="5" r="3"/><circle cx="24" cy="43" r="3"/><circle cx="5" cy="24" r="3"/><circle cx="43" cy="24" r="3"/><circle cx="10" cy="10" r="3"/><circle cx="38" cy="38" r="3"/><circle cx="38" cy="10" r="3"/><circle cx="10" cy="38" r="3"/><path d="M24 8v8M24 32v8M8 24h8M32 24h8M12 12l6 6M36 36l-6-6M36 12l-6 6M12 36l6-6"/></svg>
    <h4>Global Reach</h4>
    <p>Our platform allows companies and investors from around the world to connect and engage in share auctions effortlessly, no matter where they are located.</p>
  </div>
  <div class="card" style="left:494px;top:2772px">
    <svg width="48" height="48" viewBox="0 0 48 48" fill="none" stroke="#fff" stroke-width="1.8"><rect x="4" y="16" width="22" height="28"/><rect x="20" y="4" width="24" height="24"/><circle cx="32" cy="14" r="5"/><path d="M30 19v4h4v-4M10 34h10M10 39h10"/></svg>
    <h4>Scalability</h4>
    <p>The TenderWave platform can scale to accommodate the needs of companies of varying sizes, from startups to well-established enterprises.</p>
  </div>
  <div class="card" style="left:729px;top:2772px">
    <svg width="48" height="48" viewBox="0 0 48 48" fill="none" stroke="#fff" stroke-width="1.8"><circle cx="24" cy="22" r="18"/><path d="M6 22h36M24 4q-10 18 0 36M24 4q10 18 0 36"/><circle cx="32" cy="34" r="9" fill="#2723a6"/><path d="M32 29v10M34 31h-3a1.5 1.5 0 0 0 0 3h2a1.5 1.5 0 0 1 0 3h-3"/></svg>
    <h4>Price Discovery</h4>
    <p>Companies can maintain control over who participates in their auctions. This control is essential for preserving the company's culture, protecting sensitive information, and ensuring that only pre-approved parties are involved.</p>
  </div>
  <div class="btn-pill" style="left:514px;top:3131px"><span class="dot"></span>Contact Us Today</div>

  <h2 class="heading faq-title">Frequently <span class="accent">Asked</span> <span class="navy">Questions</span></h2>
  <div class="faq-spine"></div>
  <div class="faq-item" style="top:3434px"><div class="faq-q">Lorem ipsum dolor sit amet, consectetuer adipiscing elit, sed diam nonummy magna aliqua.<b>+</b></div><div class="faq-num">1</div></div>
  <div class="faq-item" style="top:3495px"><div class="faq-q">Consectetuer adipiscing elit, sed diam nonummy magna aliqua.<b>+</b></div><div class="faq-num">2</div></div>
  <div class="faq-item open" style="top:3557px"><div class="faq-q">Amet, consectetuer commodo consequat duisadipiscing elit, sed diam nonummy magna aliqua.<b>−</b></div><div class="faq-num">3</div></div>
  <p class="faq-answer">Duis autem vel eum iriure dolor in hendrerit in vulputate velit esse molestie consequat, vel illum dolore eu feugiat nulla facilisis at vero eros et accumsan et iusto odio dignissim qui blandit praesent luptatum zzril delenit augue duis dolore te feugait nulla facilisi.</p>
  <div class="faq-item" style="top:3677px"><div class="faq-q">Ullamcorper suscipit lobortis nisl ut aliquip ex ea commodo consequat duis autem<b>+</b></div><div class="faq-num">4</div></div>
  <div class="faq-item" style="top:3738px"><div class="faq-q">Lorem ipsum dolor sit amet, consectetuer adipiscing elit, sed diam nonummy magna aliqua.<b>+</b></div><div class="faq-num">5</div></div>

  <svg class="abs" style="left:0;top:3850px" width="1200" height="70" viewBox="0 0 1200 70">
    <path d="M142 40 Q600 0 1058 40" stroke="#0c0a93" stroke-width="6" fill="none"/>
    <path d="M0 68 Q600 10 1200 68 L1200 70 L0 70Z" fill="#0a0a3c"/>
  </svg>
  <footer>
    <div class="footer-band"></div>
    <div class="footer-row">
      <div class="contact">
        <svg width="28" height="28" viewBox="0 0 28 28" fill="none" stroke="#fff" stroke-width="1.6"><path d="M6 3l5 1 2 6-3 2q3 6 8 8l2-3 6 2 1 5q-2 3-5 3Q6 26 3 8q0-3 3-5z"/></svg>
        <div><small>Call Us</small><strong>+65 5550 0142</strong></div>
      </div>
      <div class="footer-brand"><span class="brand-dot"></span>TenderWave</div>
      <div class="contact">
        <svg width="30" height="28" viewBox="0 0 30 28" fill="none" stroke="#fff" stroke-width="1.6"><path d="M2 11l13-9 13 9v15H2z"/><path d="M2 11l13 9 13-9"/></svg>
        <div><small>Email Us</small><strong>info@tenderwave.example</strong></div>
      </div>
    </div>
    <div class="copyright-bar"><p>Copyright © 2023 TenderWave. All Rights Reserved.</p><span></span></div>
  </footer>
</div>
</body>
</html>
```